Upcoming author needs a book cover design (first in a trilogy)

I need a book cover design for my first novel. It is not yet published and I would like to present the book, complete with a cover to potential publishers. In the interim I would like to be able to use the cover as visual motivation to get it published.
The novel is called 'Any Storm, Any Harbour' and my pen name is Marisol Vey. It is a novel set in an Australian beachside town,and is about Holding Steady When the Tide Turns Against You - aimed at the Young adult market.
I want the cover to be text only (no images) and I really like the old school chalkboard design style. I particularly like the colours turquoise, fuschia pink and canary yellow together. As this is the first of 3 books, I would like the design, fonts and colours to be able to be stepped across all three covers...with one colour used predominently in each cover. For Any Storm, I would like the Turquoise blue to be the strongest colour.
I would like the cover to somehow reflect the fact that the story is set by and in the ocean without appearing 'cute/kitsch' at all.
Updates
Hello Designers,
Target Market(s)
Young adult readers - most books aimed here are black covers with dark print and imagery. I want this to be light, bright and really stand out on the shelves.
Industry/Entity Type
School
Requirements
Must have
- Ability to be printed out as A2
Should not have
- Images

```html
<!DOCTYPE html>
<html lang="en">
<head>
<meta charset="utf-8">
<title>Any Storm, Any Harbour — Cover Wrap</title>
<link rel="stylesheet" href="https://fonts.googleapis.com/css2?family=Oranienbaum&family=Crimson+Text:ital,wght@0,400;0,600;0,700;1,600&display=swap">
<style>
  :root {
    --page: #e9e9e9;
    --board-light: #f1f0ee;
    --board-mid: #d9d8d5;
    --board-dark: #c6c5c2;
    --turquoise: #1f7fa3;
    --turquoise-deep: #17678a;
    --navy: #0f4766;
    --ink: #171a1c;
    --paper: #f6f5f2;
  }
  * { box-sizing: border-box; margin: 0; padding: 0; }
  html, body { width: 1200px; height: 800px; overflow: hidden; }
  body {
    background: var(--page);
    display: flex;
    align-items: center;
    justify-content: center;
  }
  .cover-wrap {
    display: flex;
    width: 836px;
    height: 620px;
    box-shadow: 0 10px 30px rgba(0,0,0,.12);
  }
  .chalkboard {
    background:
      radial-gradient(ellipse at 30% 20%, var(--board-light) 0%, transparent 60%),
      radial-gradient(ellipse at 75% 80%, var(--board-light) 0%, transparent 55%),
      linear-gradient(160deg, var(--board-mid), var(--board-dark));
  }

  /* Back cover */
  .back-cover {
    width: 400px;
    height: 620px;
    padding: 22px 28px 30px;
    display: flex;
    flex-direction: column;
  }
  .back-author {
    align-self: flex-end;
    margin-right: 50px;
    font-family: "Crimson Text", serif;
    font-size: 12px;
    color: var(--turquoise-deep);
  }
  .back-title {
    font-family: "Oranienbaum", serif;
    font-weight: 400;
    font-size: 33px;
    line-height: 1;
    white-space: nowrap;
    color: var(--turquoise);
    text-align: center;
    margin-top: 2px;
  }
  .back-subtitle {
    font-family: "Crimson Text", serif;
    font-weight: 600;
    font-size: 13.5px;
    white-space: nowrap;
    color: var(--turquoise-deep);
    text-align: center;
    margin-top: 8px;
  }
  .back-blurb {
    font-family: "Crimson Text", serif;
    font-weight: 700;
    font-size: 12.4px;
    line-height: 1.42;
    color: var(--ink);
    text-align: justify;
    margin-top: 16px;
  }
  .back-footer {
    margin-top: auto;
    display: flex;
    justify-content: space-between;
  }
  .back-box {
    width: 104px;
    height: 58px;
    background: var(--navy);
    color: #c9d6de;
    font-family: "Crimson Text", serif;
    font-size: 12px;
    display: flex;
    align-items: center;
    justify-content: center;
    letter-spacing: .5px;
  }

  /* Spine */
  .spine {
    width: 36px;
    height: 620px;
    border-left: 1px solid rgba(0,0,0,.08);
    border-right: 1px solid rgba(0,0,0,.08);
    display: flex;
    flex-direction: column;
    align-items: center;
    justify-content: space-between;
    padding: 18px 0 22px;
  }
  .spine-title, .spine-author {
    writing-mode: vertical-rl;
    color: var(--turquoise-deep);
  }
  .spine-title {
    font-family: "Oranienbaum", serif;
    font-size: 26px;
    line-height: 1;
  }
  .spine-author {
    font-family: "Crimson Text", serif;
    font-size: 12px;
  }

  /* Front cover */
  .front-cover {
    width: 400px;
    height: 620px;
    position: relative;
  }
  .front-art { position: absolute; inset: 0; }
  .front-author {
    font-family: "Oranienbaum", serif;
    font-size: 48px;
    letter-spacing: 1px;
    fill: var(--paper);
  }
  .front-title {
    font-family: "Oranienbaum", serif;
    font-size: 56px;
    fill: var(--turquoise-deep);
  }
  .front-subtitle {
    font-family: "Crimson Text", serif;
    font-size: 19px;
    fill: var(--paper);
  }
</style>
</head>
<body>
  <main class="cover-wrap">
    <section class="back-cover chalkboard" aria-label="Back cover">
      <p class="back-author">Marisol Vey’s</p>
      <h2 class="back-title">Any Storm, Any Harbour</h2>
      <p class="back-subtitle">Holding Steady When the Tide Turns Against You</p>
      <p class="back-blurb">
        Lorem ipsum dolor sit amet, consectetur adipisicing elit, sed do eiusmod tempor incididunt ut labore et dolore magna aliqua. Ut enim ad minim veniam, quis nostrud exercitation.
        Lorem ipsum dolor sit amet, consectetur adipisicing elit, sed do eiusmod tempor incididunt ut labore et dolore magna aliqua. Ut enim ad minim veniam, quis nostrud exercitation.
        Lorem ipsum dolor sit amet, consectetur adipisicing elit, sed do eiusmod tempor incididunt ut labore et dolore magna aliqua. Ut enim ad minim veniam, quis nostrud exercitation.
        Lorem ipsum dolor sit amet, consectetur adipisicing elit, sed do eiusmod tempor incididunt ut labore et dolore magna aliqua. Ut enim ad minim veniam, quis nostrud exercitation.
        Lorem ipsum dolor sit amet, consectetur adipisicing elit, sed do eiusmod tempor incididunt ut labore et dolore magna aliqua. Ut enim ad minim veniam, quis nostrud exercitation.
        Lorem ipsum dolor sit amet, consectetur adipisicing elit, sed do eiusmod tempor incididunt ut labore et dolore magna aliqua. Ut enim ad minim veniam, quis nostrud exercitation.
      </p>
      <div class="back-footer">
        <div class="back-box">LOGO</div>
        <div class="back-box">ISBN</div>
      </div>
    </section>

    <section class="spine chalkboard" aria-label="Spine">
      <span class="spine-title">Any Storm, Any Harbour</span>
      <span class="spine-author">Marisol Vey</span>
    </section>

    <section class="front-cover chalkboard" aria-label="Front cover">
      <svg class="front-art" viewBox="0 0 400 620" width="400" height="620">
        <rect class="frame" x="14" y="14" width="372" height="592" fill="none" stroke="var(--turquoise)" stroke-width="3"/>

        <rect class="panel-top" x="36" y="36" width="328" height="214" fill="var(--turquoise)"/>
        <text class="front-author" x="200" y="160" text-anchor="middle">MARISOL VEY’S</text>

        <line x1="24" y1="264" x2="376" y2="264" stroke="var(--turquoise)" stroke-width="2"/>
        <text class="front-title" x="200" y="360" text-anchor="middle" textLength="336" lengthAdjust="spacingAndGlyphs">Any Storm, Any Harbour</text>
        <line x1="24" y1="418" x2="376" y2="418" stroke="var(--turquoise)" stroke-width="2"/>

        <rect class="panel-bottom" x="36" y="432" width="328" height="152" fill="var(--turquoise)"/>
        <text class="front-subtitle" x="200" y="500" text-anchor="middle">Holding Steady When the</text>
        <text class="front-subtitle" x="200" y="526" text-anchor="middle">Tide Turns Against You</text>
      </svg>
    </section>
  </main>
</body>
</html>
```